Real Estate Sales Brokerage

Design a modern and fresh looking standard size business card, incorporate our logo's color scheme and modern appearance with head shot photo on front side and incorporate our log on the back side

Target Market(s)

Residential Home sales

Industry/Entity Type

Real Estate Agent

Font styles to use
Sans Serif

Colors

Designer to choose colors to be used in the design.

Requirements
Must have
• fresh, modern, not too busy, incorporate head shot in front of the card, incorporate logo in front and back of the card. Use logo design scheme as appropriate.
Nice to have
• horizontal and vertical options to compare would be nice.

```html
<!DOCTYPE html>
<html lang="en">
<head>
<meta charset="utf-8">
<title>Harbor Key Realty – Business Card</title>
<link rel="stylesheet" href="https://fonts.googleapis.com/css2?family=Cinzel:wght@400;600&family=Open+Sans:ital,wght@0,400;0,600;1,400&display=swap">
<style>
  :root {
    --backdrop: #3a3a3a;
    --card: #1f1f20;
    --gold: #d9c21a;
    --olive: #6f6a0c;
    --ink: #ffffff;
    --muted: #d8d8d8;
    --photo-top: #2c2c2e;
    --photo-bottom: #2f4f94;
  }
  * { margin: 0; padding: 0; box-sizing: border-box; }
  html, body { width: 799px; height: 1200px; overflow: hidden; }
  body {
    background: var(--backdrop);
    font-family: "Open Sans", Arial, sans-serif;
    display: flex; flex-direction: column; align-items: center; justify-content: center;
    gap: 90px;
  }
  .card {
    position: relative;
    width: 700px; height: 400px;
    background: var(--card);
    border-radius: 6px;
    overflow: hidden;
    box-shadow: 0 10px 30px rgba(0,0,0,.45);
  }
  /* Back side */
  .card--back { display: flex; align-items: center; justify-content: center; }
  .brand { display: flex; align-items: center; gap: 22px; }
  .brand__square { width: 26px; height: 26px; background: var(--olive); flex: none; }
  .brand__name {
    font-family: "Cinzel", Georgia, serif;
    font-weight: 400;
    color: var(--olive);
    font-size: 44px; line-height: 1.05;
    letter-spacing: 1px;
  }
  /* Front side */
  .card--front .brand { position: absolute; left: 48px; top: 36px; gap: 14px; }
  .card--front .brand__square { width: 16px; height: 16px; }
  .card--front .brand__name { font-size: 24px; }
  .agent { position: absolute; left: 48px; top: 150px; width: 330px; }
  .agent__name {
    font-family: "Cinzel", Georgia, serif;
    font-weight: 600;
    color: var(--gold);
    font-size: 30px; letter-spacing: 1px;
    white-space: nowrap;
  }
  .agent__title { font-style: italic; color: var(--muted); font-size: 14px; margin-top: 2px; }
  .agent__address { color: var(--ink); font-size: 15px; line-height: 1.35; margin-top: 22px; }
  .contact { list-style: none; margin-top: 14px; color: var(--ink); font-size: 15px; line-height: 1.5; }
  .contact li { display: flex; align-items: center; gap: 10px; }
  .contact svg { width: 14px; height: 14px; fill: var(--gold); flex: none; }
  .headshot {
    position: absolute; right: 0; bottom: 0;
    width: 310px; height: 260px;
    background: linear-gradient(180deg, var(--photo-top) 0%, #3b4666 55%, var(--photo-bottom) 100%);
  }
</style>
</head>
<body>
  <section class="card card--back">
    <div class="brand">
      <span class="brand__square"></span>
      <div class="brand__name">Harbor Key<br>Realty</div>
    </div>
  </section>

  <section class="card card--front">
    <div class="brand">
      <span class="brand__square"></span>
      <div class="brand__name">Harbor Key<br>Realty</div>
    </div>
    <div class="agent">
      <h1 class="agent__name">Daniel Mercer</h1>
      <p class="agent__title">Managing Director</p>
      <p class="agent__address">Your Long Commercial or business<br>address in 2 line with pincode</p>
      <ul class="contact">
        <li><svg viewBox="0 0 24 24"><path d="M6.6 10.8a15 15 0 0 0 6.6 6.6l2.2-2.2a1 1 0 0 1 1-.25 11.4 11.4 0 0 0 3.6.6 1 1 0 0 1 1 1V20a1 1 0 0 1-1 1A17 17 0 0 1 3 4a1 1 0 0 1 1-1h3.5a1 1 0 0 1 1 1c0 1.25.2 2.45.6 3.6a1 1 0 0 1-.25 1z"/></svg>00-0000-000-000</li>
        <li><svg viewBox="0 0 24 24"><path d="M2 5h20v14H2zm2 2v.5l8 5 8-5V7l-8 5z"/></svg>daniel@harborkeyrealty.com</li>
        <li><svg viewBox="0 0 24 24"><circle cx="12" cy="12" r="10"/></svg>www.harborkeyrealty.com</li>
      </ul>
    </div>
    <div class="headshot" role="img" aria-label="Head shot photo of the agent"></div>
  </section>
</body>
</html>
```